Wordpress Design for a Private Label BBQ Brand

For our new brand, we'd need a new Wordpress website. We'd prefer to run the website on Wordpress

We'd like to include the following
- space for description of the brand
- space for product portfolio (not a shop!)
- space for socials
- space for support
- space for contact

```html
<!DOCTYPE html>
<html lang="en">
<head>
<meta charset="utf-8">
<title>Fornace – BBQ Brand</title>
<link rel="stylesheet" href="https://fonts.googleapis.com/css2?family=Bitter:wght@400;500;700&family=Montserrat:wght@400;600;700&display=swap">
<style>
:root{
  --red:#b8171b;
  --ink:#1f1f1f;
  --muted:#6b6b6b;
  --soft:#f6f1f1;
  --white:#ffffff;
  --footer:#1b1b1b;
  --line:#3a3a3a;
}
*{margin:0;padding:0;box-sizing:border-box}
html,body{width:1200px;height:4003px;overflow:hidden}
body{position:relative;background:var(--white);font-family:"Bitter",Georgia,serif;color:var(--ink)}
a{text-decoration:none;color:inherit}
.abs{position:absolute}
.btn{position:absolute;display:flex;align-items:center;justify-content:center;background:var(--red);color:var(--white);border-radius:30px;font-weight:700;text-transform:uppercase;font-family:"Bitter",serif;white-space:nowrap}
.rule{position:absolute;height:3px;width:46px;background:var(--red)}

/* header */
.site-header{top:0;left:0;width:1200px;height:85px;background:var(--white)}
.brand{display:flex;align-items:center;gap:10px;font-family:"Bitter",serif;font-weight:700;font-size:34px;color:var(--ink);white-space:nowrap}
.brand-dot{width:22px;height:22px;border-radius:50%;background:var(--red)}
.nav{top:22px;left:440px;display:flex;align-items:center;font-size:13px;white-space:nowrap}
.nav a{color:var(--ink);padding:10px 12px;text-transform:uppercase}
.nav a.active{color:var(--red);border:1.5px solid var(--red);border-radius:20px;padding:9px 16px;margin-right:4px}
.support{left:953px;top:22px;width:117px;height:36px;font-size:13px;font-weight:500;gap:7px}

/* hero */
.hero{top:85px;left:0;width:1200px;height:484px;background:linear-gradient(100deg,#4f7e1f 0%,#6a9a2c 40%,#5e8d25 70%,#3f6a18 100%)}
.hero-photo{right:0;top:0;width:540px;height:484px;background:radial-gradient(circle at 60% 45%,#555 0%,#2a2a2a 45%,rgba(40,40,40,0) 70%)}
.hero h1{left:260px;top:95px;font-size:62px;font-weight:700;color:var(--white)}
.hero p{left:260px;top:177px;width:360px;font-size:21px;line-height:29px;color:var(--white);font-weight:500}
.hero .btn{left:260px;top:294px;width:129px;height:42px;font-size:14px;border:2px solid var(--white)}
.dots{left:570px;top:437px;display:flex;gap:5px}
.dots span{width:11px;height:11px;border-radius:50%;border:1.5px solid var(--white)}
.dots span.on{background:var(--red)}

/* welcome */
.welcome-img{left:132px;top:626px;width:454px;height:348px;border-radius:18px;background:linear-gradient(135deg,#3b4a3a,#7d8a6a 45%,#b5b8b4 60%,#8a7a6a)}
.welcome h2{position:absolute;left:645px;top:622px;font-size:25px;font-weight:400}
.welcome .rule{left:645px;top:667px}
.welcome p{position:absolute;left:645px;top:703px;width:416px;font-size:14.5px;line-height:22.4px;color:#333}
.welcome .btn{left:645px;top:934px;width:106px;height:34px;font-size:11px}

/* products */
.products{top:1035px;left:0;width:1200px;height:863px;background:var(--soft)}
.sec-title{position:absolute;left:0;width:1200px;text-align:center;font-size:25px;font-weight:400}
.card{position:absolute;width:221px;height:266px;background:var(--white);border-radius:18px;box-shadow:0 2px 8px rgba(0,0,0,.06);overflow:hidden}
.card .shot{position:absolute;left:30px;top:30px;width:161px;height:206px;border-radius:10px;background:radial-gradient(circle,#3a3a3a 0%,#8a8a8a 55%,#ffffff 75%)}
.card .shot.wide{left:0;top:37px;width:221px;height:188px;border-radius:0;background:linear-gradient(135deg,#2b2b2b,#5a5a5a 50%,#2e2e2e)}
.plabel{position:absolute;width:221px;text-align:center;font-size:14px}
.products .btn{left:522px;top:791px;width:154px;height:34px;font-size:11px}

/* faq */
.faq h2{position:absolute;left:132px;top:1960px;font-size:25px;font-weight:400}
.faq .rule{left:132px;top:2006px}
.faq-item{position:absolute;left:132px;width:560px;height:39px;border:1.5px solid #555;border-radius:12px;display:flex;align-items:center;justify-content:space-between;padding:0 14px 0 23px;font-size:14px;color:#222;white-space:nowrap}
.faq-img{left:737px;top:1958px;width:334px;height:482px;border-radius:18px;background:linear-gradient(180deg,#d9c59a 0%,#8a7454 35%,#2a2624 60%,#7a6a58 100%)}

/* feed */
.feed{top:2517px;left:0;width:1200px;height:602px;background:var(--soft)}
.feed .rule{left:577px;top:87px}
.social{position:absolute;top:127px;width:38px;height:38px;border-radius:50%;background:var(--ink)}
.social.red{background:var(--red)}
.post{position:absolute;top:209px;width:219px;height:339px;background:var(--white);border-radius:12px;overflow:hidden}
.post .shot{height:190px}
.post h3{margin:21px 22px 0;font-family:"Montserrat",sans-serif;font-size:13.5px;line-height:17px;font-weight:700}
.post p{margin:14px 22px 0;font-family:"Montserrat",sans-serif;font-size:11px;line-height:14.5px;color:var(--muted)}

/* contact */
.contact{top:3119px;left:0;width:1200px;height:525px;background:radial-gradient(ellipse at 30% 55%,#3a2a20 0%,#4d6e22 35%,#6f9a2e 70%,#4a7420 100%)}
.contact h2{position:absolute;left:646px;top:50px;font-size:25px;font-weight:700;color:var(--white)}
.field{position:absolute;background:var(--white);border-radius:16px;font-size:13px;color:#666;padding:0 20px;display:flex;align-items:center}
.field.msg{align-items:flex-start;padding-top:20px}
.contact .btn{left:646px;top:421px;width:412px;height:48px;font-size:23px;font-weight:400;text-transform:none;border-radius:14px;border:1.5px solid var(--white)}

/* footer */
.site-footer{top:3644px;left:0;width:1200px;height:359px;background:var(--footer);color:var(--white);font-family:"Montserrat",sans-serif}
.site-footer .brand{position:absolute;left:132px;top:105px;color:var(--white);font-size:38px}
.fhead{position:absolute;top:49px;font-size:12px;font-weight:700;letter-spacing:.3px}
.frow{position:absolute;display:flex;align-items:center;gap:11px;font-size:11.5px;line-height:16px;white-space:nowrap}
.ficon{width:24px;height:24px;border-radius:50%;background:var(--white);flex:none;display:flex;align-items:center;justify-content:center}
.fmenu{position:absolute;left:797px;top:82px;list-style:none;font-size:11.5px;line-height:24px;text-transform:uppercase}
.fdivider{position:absolute;left:132px;top:261px;width:939px;height:1px;background:var(--line)}
.copyright{position:absolute;left:0;top:303px;width:1200px;text-align:center;font-size:11px}
</style>
</head>
<body>

<header class="site-header abs">
  <div class="brand abs" style="left:132px;top:20px"><span class="brand-dot"></span>FORNACE</div>
  <nav class="nav abs">
    <a class="active" href="#">Home</a><a href="#">About us</a><a href="#">Services</a><a href="#">Portfolio</a><a href="#">Social</a><a href="#">Contact us</a>
  </nav>
  <a class="btn support" href="#">
    <svg width="16" height="14" viewBox="0 0 16 14"><path d="M2 1h12a1 1 0 0 1 1 1v7a1 1 0 0 1-1 1H7l-4 3v-3H2a1 1 0 0 1-1-1V2a1 1 0 0 1 1-1z" fill="#fff"/><path d="M4 4.5h8M4 7h5" stroke="#b8171b" stroke-width="1.2"/></svg>
    SUPPORT
  </a>
</header>

<section class="hero abs">
  <div class="hero-photo abs" role="img" aria-label="Open kettle grill with spatula and fork on green lawn"></div>
  <h1 class="abs">BBQ Brand</h1>
  <p class="abs">There are many variations of passages of Lorem Ipsum available, but the majority have.</p>
  <a class="btn" href="#">Read more</a>
  <div class="dots abs"><span></span><span class="on"></span><span></span><span></span></div>
</section>

<section class="welcome">
  <div class="welcome-img abs" role="img" aria-label="Stainless steel gas grill on a wooden garden deck"></div>
  <h2>Welcome to Fornace</h2>
  <div class="rule"></div>
  <p>It is a long established fact that a reader will be distracted by the readable content of a page when looking at its layout. The point of using Lorem Ipsum is that it has a more-or-less normal distribution of letters, as opposed to using 'Content here, content here', making it look like readable English. Many desktop publishing packages and web page editors now use Lorem Ipsum as their default model text, and a search for 'lorem ipsum' will uncover many web sites still in their infancy. Various versions have evolved.</p>
  <a class="btn" href="#">Read more</a>
</section>

<section class="products abs">
  <h2 class="sec-title" style="top:36px">Our Product</h2>
  <div class="rule" style="left:589px;top:82px;width:22px"></div>

  <div class="card" style="left:132px;top:118px"><div class="shot" role="img" aria-label="Black ceramic kamado grill"></div></div>
  <div class="card" style="left:373px;top:118px"><div class="shot" role="img" aria-label="Portable tabletop grill"></div></div>
  <div class="card" style="left:611px;top:118px"><div class="shot" role="img" aria-label="Aluminium tool carry case"></div></div>
  <div class="card" style="left:849px;top:118px"><div class="shot" role="img" aria-label="Two-prong grill fork"></div></div>
  <div class="plabel" style="left:132px;top:403px">Product 1</div>
  <div class="plabel" style="left:373px;top:403px">Product 2</div>
  <div class="plabel" style="left:611px;top:403px">Product 3</div>
  <div class="plabel" style="left:849px;top:403px">Product 4</div>

  <div class="card" style="left:132px;top:449px"><div class="shot" role="img" aria-label="Grill tongs"></div></div>
  <div class="card" style="left:373px;top:449px"><div class="shot" role="img" aria-label="Silicone basting brush"></div></div>
  <div class="card" style="left:611px;top:449px"><div class="shot" role="img" aria-label="Pair of corn holders"></div></div>
  <div class="card" style="left:849px;top:449px"><div class="shot wide" role="img" aria-label="Close-up of kamado air vent"></div></div>
  <div class="plabel" style="left:132px;top:734px">Product 5</div>
  <div class="plabel" style="left:373px;top:734px">Product 6</div>
  <div class="plabel" style="left:611px;top:734px">Product 7</div>
  <div class="plabel" style="left:849px;top:734px">Product 8</div>

  <a class="btn" href="#">View all products</a>
</section>

<section class="faq">
  <h2>FAQ</h2>
  <div class="rule"></div>
  <div class="faq-item" style="top:2053px">Lorem ipsum dolor sit amet, consectetur adipiscing elit.<svg width="20" height="20" viewBox="0 0 20 20"><circle cx="10" cy="10" r="8.5" fill="none" stroke="#222" stroke-width="1.3"/><path d="M6.5 8.5l3.5 3.5 3.5-3.5" fill="none" stroke="#222" stroke-width="1.3"/></svg></div>
  <div class="faq-item" style="top:2110px">Curabitur at metus cursus, pellentesque neque non, mattis sapien.<svg width="20" height="20" viewBox="0 0 20 20"><circle cx="10" cy="10" r="8.5" fill="none" stroke="#222" stroke-width="1.3"/><path d="M6.5 8.5l3.5 3.5 3.5-3.5" fill="none" stroke="#222" stroke-width="1.3"/></svg></div>
  <div class="faq-item" style="top:2168px">Nunc euismod orci et nulla laoreet, sed varius lorem aliquam.<svg width="20" height="20" viewBox="0 0 20 20"><circle cx="10" cy="10" r="8.5" fill="none" stroke="#222" stroke-width="1.3"/><path d="M6.5 8.5l3.5 3.5 3.5-3.5" fill="none" stroke="#222" stroke-width="1.3"/></svg></div>
  <div class="faq-item" style="top:2225px">Nullam molestie ex quis nisl posuere faucibus.<svg width="20" height="20" viewBox="0 0 20 20"><circle cx="10" cy="10" r="8.5" fill="none" stroke="#222" stroke-width="1.3"/><path d="M6.5 8.5l3.5 3.5 3.5-3.5" fill="none" stroke="#222" stroke-width="1.3"/></svg></div>
  <div class="faq-item" style="top:2283px">Nunc nec turpis sit amet lorem rutrum condimentum.<svg width="20" height="20" viewBox="0 0 20 20"><circle cx="10" cy="10" r="8.5" fill="none" stroke="#222" stroke-width="1.3"/><path d="M6.5 8.5l3.5 3.5 3.5-3.5" fill="none" stroke="#222" stroke-width="1.3"/></svg></div>
  <div class="faq-item" style="top:2340px">Curabitur viverra justo nec est placerat, ut consectetur lorem pharetra.<svg width="20" height="20" viewBox="0 0 20 20"><circle cx="10" cy="10" r="8.5" fill="none" stroke="#222" stroke-width="1.3"/><path d="M6.5 8.5l3.5 3.5 3.5-3.5" fill="none" stroke="#222" stroke-width="1.3"/></svg></div>
  <div class="faq-item" style="top:2398px">Sed mattis ex nec nulla egestas dictum.<svg width="20" height="20" viewBox="0 0 20 20"><circle cx="10" cy="10" r="8.5" fill="none" stroke="#222" stroke-width="1.3"/><path d="M6.5 8.5l3.5 3.5 3.5-3.5" fill="none" stroke="#222" stroke-width="1.3"/></svg></div>
  <div class="faq-img abs" role="img" aria-label="Black kettle grill on a patio at sunset"></div>
</section>

<section class="feed abs">
  <h2 class="sec-title" style="top:38px">Feed</h2>
  <div class="rule"></div>
  <span class="social red" style="left:525px"></span>
  <span class="social" style="left:579px"></span>
  <span class="social" style="left:640px"></span>

  <article class="post" style="left:132px"><div class="shot" role="img" aria-label="Steak being placed on a hot grill" style="background:linear-gradient(160deg,#1c1c1c,#5a3a2a 60%,#2a2a2a)"></div><h3>Lorem Ipsum is simply dummy text</h3><p>There are many variations of passages of Lorem Ipsum available, but the majority have suffered</p></article>
  <article class="post" style="left:371px"><div class="shot" role="img" aria-label="Gas grill in a garden" style="background:linear-gradient(160deg,#4a6a2a,#9a9a8a 55%,#c8c0b0)"></div><h3>Lorem Ipsum is simply dummy text</h3><p>There are many variations of passages of Lorem Ipsum available, but the majority have suffered</p></article>
  <article class="post" style="left:614px"><div class="shot" role="img" aria-label="Kettle grill with tools on grass" style="background:linear-gradient(120deg,#5f8f24,#6a9a2c 45%,#2a2a2a 75%)"></div><h3>Lorem Ipsum is simply dummy text</h3><p>There are many variations of passages of Lorem Ipsum available, but the majority have suffered</p></article>
  <article class="post" style="left:849px"><div class="shot" role="img" aria-label="Row of barrel grills in a store" style="background:linear-gradient(160deg,#3a3a3a,#1e1e1e 55%,#6a6a6a)"></div><h3>Lorem Ipsum is simply dummy text</h3><p>There are many variations of passages of Lorem Ipsum available, but the majority have suffered</p></article>
</section>

<section class="contact abs" role="img" aria-label="Grill loaded with meat and vegetables on a lawn">
  <h2>Contact us</h2>
  <div class="field" style="left:646px;top:121px;width:203px;height:41px">First Name</div>
  <div class="field" style="left:856px;top:121px;width:202px;height:41px">Last Name</div>
  <div class="field" style="left:646px;top:177px;width:412px;height:40px">Email id</div>
  <div class="field" style="left:646px;top:230px;width:412px;height:40px">Phone</div>
  <div class="field msg" style="left:646px;top:286px;width:412px;height:115px">Message</div>
  <a class="btn" href="#">Submit</a>
</section>

<footer class="site-footer abs">
  <div class="brand"><span class="brand-dot"></span>FORNACE</div>

  <div class="fhead" style="left:451px">CONTACT US</div>
  <div class="frow" style="left:451px;top:83px"><span class="ficon"><svg width="12" height="12" viewBox="0 0 12 12"><path d="M6 1a3.5 3.5 0 0 1 3.5 3.5C9.5 7 6 11 6 11S2.5 7 2.5 4.5A3.5 3.5 0 0 1 6 1z" fill="#1b1b1b"/><circle cx="6" cy="4.5" r="1.2" fill="#fff"/></svg></span><span>Unit 4, Level 2,<br>210-214 Ember Lane, Ashfield NSW 2131.</span></div>
  <div class="frow" style="left:451px;top:134px"><span class="ficon"><svg width="12" height="12" viewBox="0 0 12 12"><path d="M3 1.5l1.8 2.3-1 1.2a6 6 0 0 0 3.2 3.2l1.2-1 2.3 1.8-1 1.5C5.5 10.5 1.5 6.5 1.5 2.5z" fill="#1b1b1b"/></svg></span><span>Call Us<br>+1 555 010 0199</span></div>
  <div class="frow" style="left:451px;top:185px"><span class="ficon"><svg width="12" height="10" viewBox="0 0 12 10"><rect x="1" y="1" width="10" height="8" rx="1" fill="#1b1b1b"/><path d="M1.5 1.8L6 5.5l4.5-3.7" stroke="#fff" fill="none"/></svg></span><span>E mail Us<br>hello@fornace.example</span></div>

  <div class="fhead" style="left:797px">MENU</div>
  <ul class="fmenu"><li>Home</li><li>About us</li><li>Services</li><li>Portfolio</li><li>Social</li><li>Contact us</li></ul>

  <div class="fhead" style="left:973px">FOLLOW US</div>
  <div class="frow" style="left:973px;top:84px"><span class="ficon"></span><span>Like us on<br>EMBERBOOK</span></div>
  <div class="frow" style="left:973px;top:134px"><span class="ficon"></span><span>Follow us on<br>CHIRPLINE</span></div>
  <div class="frow" style="left:973px;top:185px"><span class="ficon"></span><span>Follow us on<br>WORKLINK</span></div>

  <div class="fdivider"></div>
  <div class="copyright">Copyright © 2023 All Rights Reserved</div>
</footer>

</body>
</html>
```